Most captivating card ever!

Life Coach - Professional Adventurer - Entrepreneur
I need the worlds most amazing business card for my personal brand. This business card will mostly be used to give to prospective clients for life coaching and business coaching.
Be creative, be adventurous. It needs to stand out. Make people say.. I need this guy!
My background is as an entrepreneur and professional adventurer undertaking extreme expeditions. I am now moving into life coaching.
No specific design ideas, so you have full creativity. Show me your best.
Industry/Entity Type
Life Coaching
Contact Information for Business Card
Dan Pellow
itsdanp.com.au
0468215903
Colors
Designer to choose colors to be used in the design.
Look and feel

```html
<!DOCTYPE html>
<html lang="en">
<head>
<meta charset="utf-8">
<title>Dan Pellow – Life Coach Business Card</title>
<link href="https://fonts.googleapis.com/css2?family=Questrial&display=swap" rel="stylesheet">
<style>
  :root {
    --backdrop: #d4d4d4;
    --silver-light: #f2f2f3;
    --silver-mid: #c9c9cc;
    --silver-dark: #9d9da1;
    --green: #1f9a3e;
    --green-deep: #0f6a32;
    --shadow: rgba(0,0,0,0.22);
  }
  * { margin: 0; padding: 0; box-sizing: border-box; }
  html, body {
    width: 1200px; height: 960px; overflow: hidden;
    background: var(--backdrop);
    font-family: "Questrial", sans-serif;
  }
  .canvas {
    width: 1200px; height: 960px;
    display: flex; flex-direction: column;
    align-items: center; justify-content: center; gap: 56px;
  }
  .card {
    position: relative;
    width: 660px; height: 377px;
    background: linear-gradient(115deg, var(--silver-dark) 0%, var(--silver-mid) 30%, var(--silver-light) 55%, var(--silver-mid) 80%, var(--silver-dark) 100%);
    box-shadow: 0 14px 30px var(--shadow);
    overflow: hidden;
    color: var(--green);
    text-align: center;
  }
  .card-curves { position: absolute; inset: 0; width: 100%; height: 100%; }
  .brand-name {
    position: absolute; left: 0; right: 0;
    font-size: 58px; line-height: 1; color: var(--green);
    letter-spacing: 1px;
  }
  .card-front .brand-name { top: 52px; }
  .card-back .brand-name { top: 140px; }
  .holder {
    position: absolute; left: 0; right: 0; top: 150px;
    line-height: 1.25;
  }
  .holder-name { font-size: 28px; color: var(--green-deep); }
  .holder-role { font-size: 17px; letter-spacing: 6px; color: var(--green-deep); margin-bottom: 8px; }
  .holder-contact { font-size: 17px; color: var(--green); }
  .tagline {
    position: absolute; left: 0; right: 0; bottom: 28px;
    font-size: 15px; letter-spacing: 0.5px; color: var(--green);
  }
</style>
</head>
<body>
<main class="canvas">
  <section class="card card-front" aria-label="Business card front">
    <svg class="card-curves" viewBox="0 0 660 377" preserveAspectRatio="none" aria-hidden="true">
      <defs>
        <linearGradient id="sweepTop" x1="0" y1="0" x2="1" y2="1">
          <stop offset="0" stop-color="#8f8f94"/>
          <stop offset="1" stop-color="#e6e6e8"/>
        </linearGradient>
        <linearGradient id="sweepBottom" x1="1" y1="1" x2="0" y2="0">
          <stop offset="0" stop-color="#8f8f94"/>
          <stop offset="1" stop-color="#f4f4f5"/>
        </linearGradient>
      </defs>
      <path d="M0 0 H190 Q120 40 0 150 Z" fill="url(#sweepTop)"/>
      <path d="M660 377 H450 Q560 330 660 190 Z" fill="url(#sweepBottom)"/>
    </svg>
    <div class="brand-name">Life Coach</div>
    <div class="holder">
      <div class="holder-name">Dan Pellow</div>
      <div class="holder-role">Life Coach</div>
      <div class="holder-contact">0468215903</div>
      <div class="holder-contact">itsdanp.com.au</div>
    </div>
    <p class="tagline">Life Coach - Professional Adventurer - Entrepreneur</p>
  </section>

  <section class="card card-back" aria-label="Business card back">
    <svg class="card-curves" viewBox="0 0 660 377" preserveAspectRatio="none" aria-hidden="true">
      <defs>
        <linearGradient id="sweepBack" x1="0" y1="0" x2="1" y2="1">
          <stop offset="0" stop-color="#8f8f94"/>
          <stop offset="1" stop-color="#ececee"/>
        </linearGradient>
      </defs>
      <path d="M0 0 H130 Q40 110 0 300 Z" fill="url(#sweepBack)"/>
    </svg>
    <div class="brand-name">Life Coach</div>
    <p class="tagline">Life Coach - Professional Adventurer - Entrepreneur</p>
  </section>
</main>
</body>
</html>
```